Design business cards for Ironvale Barbers (Opening March so won't need finalised till January2018

Ironvale Barbers is the new age barbers and skincare for all men. Creating tailor made haircuts & customised skincare solutions for the perfect healthy manly look. The Barbers will have a industrial, rustic, worldly feel about it. Rustic red brick wall with old wine barrels as the work stations with the old fashion barber chairs. Concrete floor and a bit corrugated iron around.
Target Market(s)
Professional males who like a great haircut, wet shave and may consider a facial if in the right environment. Total pampering experience in a boys environment.
Industry/Entity Type
Barber
Contact Information for Business Card
Front- Logo - address is 42 Kowhai Rd Taupo
Ph - (07) 548 9163
www.ironvalebarbers.com
email - hello@ironvale.co.nz
Back of card
Mens Haircare - Wet Shaving - Facials - Skin Prescriptions
We are doing a loyalty program - 6 squares numbered then 7th free
Colors
Designer to choose colors to be used in the design.
Requirements
Must have
- Clean simple easy to read.
Nice to have
- Our current colours are white font on black background but thinking we need to introduce another colour. Maybe white logo on a copper, bronze or rusty background. Or even a rustic red brick wall with white writing. Want it clean simple to read. Maybe a burgundy?
Should not have
- no images like heads, scissors, razors please

```html
<!DOCTYPE html>
<html lang="en">
<head>
<meta charset="utf-8">
<title>Ironvale Barbers – Business Card</title>
<link href="https://fonts.googleapis.com/css2?family=Smokum&display=swap" rel="stylesheet">
<style>
  :root {
    --page-bg: #1b1b1b;
    --card-black: #232323;
    --card-black-deep: #141414;
    --ink-white: #f4f1ec;
    --accent-red: #9b1c1c;
    --brick-light: #b9774a;
    --brick-mid: #8f5634;
    --brick-dark: #5a3a28;
    --slip-white: #ffffff;
  }
  * { margin: 0; padding: 0; box-sizing: border-box; }
  html, body {
    width: 1200px;
    height: 897px;
    overflow: hidden;
    background: var(--page-bg);
    font-family: "Smokum", Georgia, serif;
  }
  .canvas { position: relative; width: 1200px; height: 897px; }

  .card {
    position: absolute;
    left: 303px;
    width: 594px;
    height: 338px;
    overflow: hidden;
  }

  /* Front */
  .card--front {
    top: 92px;
    background: radial-gradient(ellipse at 65% 30%, #2f2f2f 0%, var(--card-black) 45%, var(--card-black-deep) 100%);
  }
  .brand-name {
    position: absolute;
    left: 0; right: 0;
    top: 72px;
    text-align: center;
    color: var(--ink-white);
    line-height: 1;
  }
  .brand-name__main { display: block; font-size: 70px; letter-spacing: 1px; }
  .brand-name__sub { display: block; font-size: 26px; letter-spacing: 9px; margin-top: 8px; }

  .contact {
    position: absolute;
    top: 254px;
    color: var(--ink-white);
    font-size: 19px;
    line-height: 29px;
    letter-spacing: 0.3px;
    white-space: nowrap;
  }
  .contact--left { left: 39px; }
  .contact--right { left: 281px; }
  .contact__divider {
    position: absolute;
    left: 257px;
    top: 254px;
    width: 3px;
    height: 44px;
    background: var(--accent-red);
  }

  /* Back */
  .card--back { top: 470px; }
  .brick-wall {
    position: absolute;
    inset: 0;
    background:
      linear-gradient(180deg, rgba(0,0,0,0.05) 0%, rgba(0,0,0,0.28) 100%),
      linear-gradient(120deg, var(--brick-light) 0%, var(--brick-mid) 55%, var(--brick-dark) 100%);
  }
  .services {
    position: absolute;
    left: 0; right: 0;
    top: 138px;
    text-align: center;
    color: var(--ink-white);
    font-size: 27px;
    line-height: 36px;
    letter-spacing: 0.6px;
  }
  .appointment-slip {
    position: absolute;
    left: 38px;
    top: 272px;
    width: 520px;
    height: 40px;
    background: var(--slip-white);
    color: var(--accent-red);
    font-size: 21px;
    line-height: 40px;
    padding-left: 11px;
    white-space: nowrap;
    letter-spacing: 0.5px;
  }
</style>
</head>
<body>
<main class="canvas">

  <section class="card card--front" aria-label="Card front">
    <h1 class="brand-name">
      <span class="brand-name__main">IRONVALE</span>
      <span class="brand-name__sub">BARBERS</span>
    </h1>

    <address class="contact contact--left" style="font-style:normal">
      <div>CELL: (07) 548 9163</div>
      <div>42 KOWHAI RD TAUPO</div>
    </address>
    <span class="contact__divider"></span>
    <address class="contact contact--right" style="font-style:normal">
      <div>HELLO@IRONVALE.CO.NZ</div>
      <div>WWW.IRONVALEBARBERS.COM</div>
    </address>
  </section>

  <section class="card card--back" aria-label="Card back">
    <div class="brick-wall" role="img" aria-label="Rustic red brick wall photograph"></div>
    <p class="services">
      MENS HAIRCARE - WET SHAVING<br>
      FACIALS - SKIN PRESCRIPTIONS
    </p>
    <div class="appointment-slip">DATE: _ _ / _ _ / _ _ _ _ _TIME: _ _ _ _ _ _ _ _ _</div>
  </section>

</main>
</body>
</html>
```